Gardener needs an exciting new flyer design.

I'm a passionate gardener that requires a custom flyer design for a owner operator gardening business. Design will be for a DL flyer. I'm based on the Sunshine coast in Queensland Australia. My target audience is the residential market on the Sunshine coast. Business name is Marlowe Greens. My services are, lawn mowing, weeding, Eco Friendly fertilizing, green waste removal, Mulching, tree and shrub pruning, Full garden makeovers, hedging, pressure cleaning, privacy screening, Timber deck rejuvenation, Planting, Turf preparation and installation, and much more. Free no obligation quotes, reliable and friendly service, great rates. 12 years experience. Web www.marlowegreens.com.au - Phone 0418527064 - Email doug@marlowegreens.com.au I would like the design to portray a friendly and professional approach.

Target Market(s)

Residential

Industry/Entity Type

Gardener

Font styles to use
Serif

Colors
9ccb3b
abd037
3176b5

Requirements
Must have
• my services, my logo, my contact details,

```html
<!DOCTYPE html>
<html lang="en">
<head>
<meta charset="utf-8">
<title>Marlowe Greens – DL Flyer</title>
<link rel="stylesheet" href="https://fonts.googleapis.com/css2?family=Montserrat:wght@400;500;700&family=Open+Sans:wght@400;700&display=swap">
<style>
  :root {
    --blue: #3f68b1;
    --green: #8dc63f;
    --white: #ffffff;
    --backdrop: #6f6767;
    --garden-purple: #7c6bc4;
    --garden-green: #3f8a3a;
    --home-green: #5e9f4c;
    --home-green-light: #74ad62;
  }
  * { margin: 0; padding: 0; box-sizing: border-box; }
  html, body { width: 672px; height: 1200px; overflow: hidden; background: var(--backdrop); }
  .canvas { position: relative; width: 672px; height: 1200px; }
  .flyer {
    position: absolute; left: 66px; top: 24px;
    width: 676px; height: 1440px;
    transform: scale(0.8); transform-origin: 0 0;
    overflow: hidden; background: var(--blue);
    font-family: "Montserrat", sans-serif; color: var(--white);
  }
  .flyer-art { position: absolute; inset: 0; }
  .intro { position: absolute; left: 44px; top: 30px; width: 282px; }
  .intro-title { font-family: "Open Sans", sans-serif; font-weight: 700; font-size: 30px; line-height: 40px; margin-bottom: 8px; }
  .intro-copy { font-size: 21.5px; line-height: 29px; }
  .brand-mark {
    position: absolute; left: 444px; top: 470px; width: 160px; height: 100px;
    display: flex; align-items: center; justify-content: center; text-align: center;
    font-weight: 700; font-size: 24px; line-height: 28px; color: var(--blue);
  }
  .services { position: absolute; left: 343px; top: 638px; }
  .services-title { font-weight: 700; font-size: 31px; line-height: 40px; margin-left: 2px; margin-bottom: 4px; }
  .service-list { list-style: none; }
  .service-list li { display: flex; align-items: center; height: 33.8px; font-size: 21px; letter-spacing: 0.2px; }
  .service-list svg { width: 20px; height: 20px; margin-right: 16px; flex: none; }
  .contact { position: absolute; left: 48px; top: 1160px; }
  .contact-title { font-weight: 700; font-size: 25px; line-height: 34px; margin-left: 3px; margin-bottom: 8px; }
  .contact-list { list-style: none; font-family: "Open Sans", sans-serif; font-size: 22px; }
  .contact-list li { display: flex; align-items: center; height: 53px; }
  .contact-icon { width: 40px; height: 36px; border: 2px solid var(--white); display: flex; align-items: center; justify-content: center; margin-right: 22px; flex: none; }
  .contact-icon svg { width: 24px; height: 24px; }
  .contact-phone .contact-icon { margin-right: 28px; }
</style>
</head>
<body>
<div class="canvas">
  <div class="flyer">
    <svg class="flyer-art" viewBox="0 0 676 1440" width="676" height="1440">
      <defs>
        <linearGradient id="gardenTones" x1="0" y1="0" x2="1" y2="1">
          <stop offset="0" stop-color="#5e9a4a"/>
          <stop offset="0.5" stop-color="var(--garden-purple)"/>
          <stop offset="1" stop-color="var(--garden-green)"/>
        </linearGradient>
        <linearGradient id="homeTones" x1="0" y1="0" x2="1" y2="1">
          <stop offset="0" stop-color="var(--home-green-light)"/>
          <stop offset="1" stop-color="var(--home-green)"/>
        </linearGradient>
      </defs>
      <polygon points="0,0 676,0 676,540 0,700" fill="url(#gardenTones)" role="img" aria-label="Photo of a flowering garden with lavender and a stone path"/>
      <polygon points="0,690 676,515 676,1440 0,1440" fill="var(--blue)"/>
      <polygon points="0,672 676,532 676,560 0,712" fill="var(--green)"/>
      <polygon points="22,15 338,15 338,572 22,640" fill="var(--blue)"/>
      <circle cx="524" cy="520" r="110" fill="var(--blue)"/>
      <circle cx="524" cy="520" r="96" fill="var(--green)"/>
      <circle cx="524" cy="520" r="88" fill="var(--white)"/>
      <polygon points="21,715 328,658 323,1140 21,1055" fill="url(#homeTones)" role="img" aria-label="Photo of a home with a neat lawn and trimmed hedges"/>
      <polygon points="0,1062 676,1258 676,1290 0,1092" fill="var(--green)"/>
    </svg>

    <section class="intro">
      <h1 class="intro-title">Marlowe Greens</h1>
      <p class="intro-copy">Marlowe Greens is your garden and lawn care specialist, with a passion for gardening and a keen eye for detail you can rest assured you're in the right hands.<br>My services are tailored to meet every individual clients needs.From a one time mow too regular lawn mowing, all aspects of garden care and even full garden makeovers.<br>I go that extra mile every time to leave you garden and yard looking amazing.</p>
    </section>

    <div class="brand-mark">Marlowe<br>Greens</div>

    <section class="services">
      <h2 class="services-title">Our Services</h2>
      <ul class="service-list">
        <li><svg viewBox="0 0 20 20"><rect x="1.5" y="3.5" width="15" height="15" fill="none" stroke="#fff" stroke-width="2.4"/><path d="M5 10l4 4 9-11" fill="none" stroke="#fff" stroke-width="2.8"/></svg>Lawn mowing</li>
        <li><svg viewBox="0 0 20 20"><rect x="1.5" y="3.5" width="15" height="15" fill="none" stroke="#fff" stroke-width="2.4"/><path d="M5 10l4 4 9-11" fill="none" stroke="#fff" stroke-width="2.8"/></svg>Weeding</li>
        <li><svg viewBox="0 0 20 20"><rect x="1.5" y="3.5" width="15" height="15" fill="none" stroke="#fff" stroke-width="2.4"/><path d="M5 10l4 4 9-11" fill="none" stroke="#fff" stroke-width="2.8"/></svg>Eco Friendly fertilizing</li>
        <li><svg viewBox="0 0 20 20"><rect x="1.5" y="3.5" width="15" height="15" fill="none" stroke="#fff" stroke-width="2.4"/><path d="M5 10l4 4 9-11" fill="none" stroke="#fff" stroke-width="2.8"/></svg>Green waste removal</li>
        <li><svg viewBox="0 0 20 20"><rect x="1.5" y="3.5" width="15" height="15" fill="none" stroke="#fff" stroke-width="2.4"/><path d="M5 10l4 4 9-11" fill="none" stroke="#fff" stroke-width="2.8"/></svg>Mulching</li>
        <li><svg viewBox="0 0 20 20"><rect x="1.5" y="3.5" width="15" height="15" fill="none" stroke="#fff" stroke-width="2.4"/><path d="M5 10l4 4 9-11" fill="none" stroke="#fff" stroke-width="2.8"/></svg>Tree and shrub pruning</li>
        <li><svg viewBox="0 0 20 20"><rect x="1.5" y="3.5" width="15" height="15" fill="none" stroke="#fff" stroke-width="2.4"/><path d="M5 10l4 4 9-11" fill="none" stroke="#fff" stroke-width="2.8"/></svg>Full garden makeovers</li>
        <li><svg viewBox="0 0 20 20"><rect x="1.5" y="3.5" width="15" height="15" fill="none" stroke="#fff" stroke-width="2.4"/><path d="M5 10l4 4 9-11" fill="none" stroke="#fff" stroke-width="2.8"/></svg>Hedging</li>
        <li><svg viewBox="0 0 20 20"><rect x="1.5" y="3.5" width="15" height="15" fill="none" stroke="#fff" stroke-width="2.4"/><path d="M5 10l4 4 9-11" fill="none" stroke="#fff" stroke-width="2.8"/></svg>Pressure cleaning</li>
        <li><svg viewBox="0 0 20 20"><rect x="1.5" y="3.5" width="15" height="15" fill="none" stroke="#fff" stroke-width="2.4"/><path d="M5 10l4 4 9-11" fill="none" stroke="#fff" stroke-width="2.8"/></svg>Privacy screening</li>
        <li><svg viewBox="0 0 20 20"><rect x="1.5" y="3.5" width="15" height="15" fill="none" stroke="#fff" stroke-width="2.4"/><path d="M5 10l4 4 9-11" fill="none" stroke="#fff" stroke-width="2.8"/></svg>Timber deck rejuvenation</li>
        <li><svg viewBox="0 0 20 20"><rect x="1.5" y="3.5" width="15" height="15" fill="none" stroke="#fff" stroke-width="2.4"/><path d="M5 10l4 4 9-11" fill="none" stroke="#fff" stroke-width="2.8"/></svg>Planting</li>
        <li><svg viewBox="0 0 20 20"><rect x="1.5" y="3.5" width="15" height="15" fill="none" stroke="#fff" stroke-width="2.4"/><path d="M5 10l4 4 9-11" fill="none" stroke="#fff" stroke-width="2.8"/></svg>Turf preparation and</li>
        <li><svg viewBox="0 0 20 20"><rect x="1.5" y="3.5" width="15" height="15" fill="none" stroke="#fff" stroke-width="2.4"/><path d="M5 10l4 4 9-11" fill="none" stroke="#fff" stroke-width="2.8"/></svg>installation</li>
      </ul>
    </section>

    <section class="contact">
      <h2 class="contact-title">Contact Us</h2>
      <ul class="contact-list">
        <li class="contact-phone">
          <span class="contact-icon"><svg viewBox="0 0 24 24"><path d="M4 9c0-3 3-4 8-4s8 1 8 4l-3 1-1-2H8L7 10zM6 11h12l1 8H5z" fill="#fff"/><circle cx="12" cy="15" r="2.2" fill="var(--blue)"/></svg></span>
          0418527064
        </li>
        <li>
          <span class="contact-icon"><svg viewBox="0 0 24 24" fill="none" stroke="#fff" stroke-width="1.8"><circle cx="12" cy="12" r="9"/><ellipse cx="12" cy="12" rx="4" ry="9"/><path d="M3 12h18M5 7h14M5 17h14"/></svg></span>
          WWW.MARLOWEGREENS.COM.AU
        </li>
        <li>
          <span class="contact-icon"><svg viewBox="0 0 24 24" fill="none" stroke="#fff" stroke-width="1.8"><rect x="2.5" y="5.5" width="19" height="13"/><path d="M2.5 5.5l9.5 8 9.5-8M2.5 18.5l7-6.5M21.5 18.5l-7-6.5"/></svg></span>
          DOUG@MARLOWEGREENS.COM.AU
        </li>
        <li>
          <span class="contact-icon"><svg viewBox="0 0 24 24"><path d="M12 2a6 6 0 0 0-6 6c0 4.5 6 11 6 11s6-6.5 6-11a6 6 0 0 0-6-6z" fill="#fff"/><circle cx="12" cy="8" r="2.4" fill="var(--blue)"/><path d="M4 19.5h16" stroke="#fff" stroke-width="2"/></svg></span>
          SUNSHINE COAST , QUEENSLAND, AUSTRALIA
        </li>
      </ul>
    </section>
  </div>
</div>
</body>
</html>
```